Website for Painting Company

Hi,
We are after a Wordpress website design with CSS/HTML Theme for our painting company based in Brisbane, Australia. Our business name is Felix Morrow Painting Contractors and we have been trading for 33 years.
We want a website that is modern and fresh with a professional image. Our organisation does Commercial, Residential and Insurance Painting projects. I have listed a couple of similar websites that we like the look and feel of. These are a guide only and we are happy to see you own designs with a similar professional image.
http://www.kelbrookcoatings.com.au/
http://www.tidewellfinishes.com.au/
We are a member of Guild Decorators Australia and I have supplied the logo named "gda" which I have included in the files I have uploaded.
We want a five page site. These are Home Page, Residential, Commercial, Insurance and Contact Us.
I have also uploaded our logo and some pictures labeled Logo,Residential, Commercial, Insurance and Homepage. These should be used on each page listed above.
Updates
Project Deadline Extended
Reason: We are extending because we need more time to go through the designs and give feedback. There are many fantastic designs. Thank you everyone who has contributed!!!!
All the best
Derek
Industry/Entity Type
Painting
Requirements
Must have
- We want a five page site. These are Home Page, Residential, Commercial, Insurance and Contact Us.

```html
<!DOCTYPE html>
<html lang="en">
<head>
<meta charset="utf-8">
<title>Felix Morrow &amp; Co. – Painting Contractors</title>
<link rel="stylesheet" href="https://fonts.googleapis.com/css2?family=Montserrat:wght@400;600;700&family=Cinzel:wght@400;600&family=Rokkitt:wght@400&family=Open+Sans:wght@400;600&family=Arimo:wght@400&display=swap">
<style>
:root{
  --page:#f1f1f1;
  --ink:#2b2b2b;
  --body:#444;
  --muted:#6a6a6a;
  --red:#d9261c;
  --orange:#e4531b;
  --nav-red:#e8321a;
  --nav-home:#f5a800;
  --nav-res:#0f9a48;
  --nav-com:#1c8bd6;
  --nav-ins:#f2877a;
  --nav-con:#9bcc55;
  --footer:#2a2a2a;
  --footer-text:#bdbdbd;
  --gold:#f5a800;
  --green:#4a9a2e;
  --beige:#ece4cf;
}
*{box-sizing:border-box;margin:0;padding:0}
html,body{width:920px;height:1200px;overflow:hidden}
body{background:linear-gradient(180deg,#f6f6f6 0,#efefef 60%,#f4f4f4 100%);font-family:"Open Sans",Arial,sans-serif;color:var(--body);position:relative}
.abs{position:absolute}

.hero-smoke{left:270px;top:0;width:460px;height:112px;border-radius:0 0 50% 50%/0 0 60% 60%;
  background:radial-gradient(ellipse at 30% 20%,rgba(190,80,170,.35),transparent 60%),radial-gradient(ellipse at 75% 40%,rgba(150,170,60,.35),transparent 60%),radial-gradient(ellipse at 55% 70%,rgba(230,120,60,.25),transparent 60%)}

.brand{left:115px;top:40px;display:flex;align-items:center;gap:10px}
.brand-mark{width:26px;height:26px;background:var(--red)}
.brand-name{font-family:"Montserrat",sans-serif;font-weight:700;font-size:20px;line-height:24px;color:var(--red);width:120px}

.call{left:617px;top:48px;display:flex;gap:11px}
.call-label{font-family:"Montserrat",sans-serif;font-size:20px;color:#555;line-height:22px}
.call-number{font-family:"Montserrat",sans-serif;font-weight:700;font-size:19px;color:var(--orange);line-height:24px}

.nav{left:108px;top:143px;width:704px;height:15px;display:flex;background:var(--nav-red)}
.nav-spacer{flex:0 0 335px}
.nav a{display:block;height:15px;line-height:15px;color:#fff;font-family:"Open Sans",sans-serif;font-size:10px;text-align:center;text-decoration:none}
.nav .home{width:56px;background:var(--nav-home)}
.nav .res{width:78px;background:var(--nav-res)}
.nav .com{width:82px;background:var(--nav-com)}
.nav .ins{width:73px;background:var(--nav-ins)}
.nav .con{width:80px;background:var(--nav-con)}

.slider{left:108px;top:172px;width:704px;height:312px;background:#fff;box-shadow:0 1px 4px rgba(0,0,0,.18)}
.slide-photo{position:absolute;left:8px;top:8px;width:687px;height:295px;
  background:linear-gradient(180deg,#d9d6d2 0,#c9c3bb 35%,#e7e4e0 70%,#cfcac4 100%)}
.slide-caption{position:absolute;left:8px;top:247px;width:687px;height:56px;background:rgba(40,40,40,.55);
  color:#fff;font-family:"Rokkitt",serif;font-size:17px;line-height:56px;padding-left:18px}
.slide-arrow{position:absolute;top:135px;width:27px;height:26px;background:#fff}
.slide-arrow.prev{left:23px}.slide-arrow.next{left:654px}
.slide-arrow svg{display:block}

.service{top:510px;width:212px}
.service-head{display:flex;align-items:center;gap:9px;height:42px}
.service-icon{width:40px;height:42px;border-radius:3px}
.service-title{font-family:"Montserrat",sans-serif;font-size:19px;color:var(--ink)}
.service ul{list-style:none;margin-top:10px}
.service li{font-size:10px;line-height:21.5px;color:#333;padding-left:16px;position:relative}
.service li svg{position:absolute;left:0;top:7px}
.service-rule{margin-top:8px;border-top:2px solid #d6d6d6;position:relative;height:18px}
.read-more{position:absolute;right:0;top:-1px;height:17px;padding:0 5px;background:#e9e9e9;font-size:8px;line-height:17px;color:var(--red)}

.welcome{left:109px;top:668px}
.welcome h1{font-family:"Cinzel",serif;font-weight:400;font-size:24px;line-height:26px;color:var(--ink)}
.welcome h1 span{display:block;color:var(--red)}
.welcome p{margin-top:13px;width:432px;font-size:10.2px;line-height:14.5px;color:#333}

.reasons-title{left:109px;top:824px;font-family:"Cinzel",serif;font-weight:600;font-size:15px;color:var(--ink)}
.reason{top:858px;width:150px;text-align:center}
.reason svg{display:block;margin:0 auto}
.reason-text{font-family:"Arimo",sans-serif;font-size:16px;line-height:19px;color:#777;margin-top:8px}
.reason-text strong{display:block;font-weight:400;color:var(--red)}

.quote{left:599px;top:677px;width:213px;height:127px;background:#fff;box-shadow:0 1px 4px rgba(0,0,0,.18)}
.quote-art{position:absolute;left:16px;top:8px;width:185px;height:104px;
  background:radial-gradient(ellipse at 40% 55%,rgba(220,40,40,.75),rgba(240,140,140,.35) 55%,transparent 75%)}
.quote-bar{position:absolute;left:8px;top:98px;width:198px;height:21px;background:#4a4a4a;border-radius:3px;
  color:#fff;font-family:"Montserrat",sans-serif;font-weight:700;font-size:10.5px;line-height:21px;padding-left:7px;letter-spacing:.3px}
.quote-bar svg{position:absolute;right:6px;top:3px}

.badge{left:600px;top:838px;width:210px;height:160px;background:#fff;box-shadow:0 1px 4px rgba(0,0,0,.15)}
.badge-shape{position:absolute;left:28px;top:16px;width:154px;height:128px;background:#e3e8f4;border-radius:4px}

.footer{left:0;top:1053px;width:920px;height:147px;background:var(--footer)}
.footer-links{left:108px;top:28px}
.footer h4{font-family:"Montserrat",sans-serif;font-size:10px;font-weight:600;color:var(--gold);letter-spacing:.3px}
.footer-links ul{list-style:none;margin-top:5px}
.footer-links li{font-size:8px;line-height:16px;color:#fff}
.footer-contact{left:329px;top:28px;font-size:8.5px;line-height:16px;color:var(--footer-text);font-weight:600}
.footer-call{margin-top:10px;font-family:"Montserrat",sans-serif;font-size:11px;line-height:13px;color:#fff;font-weight:400}
.footer-call b{display:block;color:var(--gold);font-weight:600}
.footer-copy{left:590px;top:28px;font-size:7.8px;color:var(--footer-text)}
.footer-follow{left:590px;top:78px;font-size:8px;color:var(--footer-text);display:flex;align-items:center;gap:5px}
.social{width:11px;height:11px;background:#3b6fb6;display:inline-block}
</style>
</head>
<body>

<div class="abs hero-smoke" role="img" aria-label="Soft coloured paint smoke swirls in violet, olive and orange"></div>

<div class="abs brand">
  <span class="brand-mark"></span>
  <span class="brand-name">Felix Morrow &amp; Co.</span>
</div>

<div class="abs call">
  <svg width="36" height="36" viewBox="0 0 36 36" aria-hidden="true">
    <path d="M3 12c0-5 7-7 15-7s15 2 15 7v3h-8v-4c-2-1-4-1-7-1s-5 0-7 1v4H3z" fill="#3a3a3a"/>
    <path d="M8 17h20l4 15H4z" fill="#3a3a3a"/>
    <circle cx="18" cy="24" r="4" fill="#f3f3f3"/>
  </svg>
  <div>
    <div class="call-label">Call NOW!</div>
    <div class="call-number">(07) 3190 4826</div>
  </div>
</div>

<nav class="abs nav">
  <span class="nav-spacer"></span>
  <a class="home" href="#">Home</a>
  <a class="res" href="#">Residential</a>
  <a class="com" href="#">Commercial</a>
  <a class="ins" href="#">Insurance</a>
  <a class="con" href="#">Contact Us</a>
</nav>

<section class="abs slider">
  <div class="slide-photo" role="img" aria-label="Bright freshly painted open-plan living and dining room"></div>
  <div class="slide-caption">"Neque porro quisquam est qui dolorem ipsum quia dolor sit amet, consectetur, adipisci..."</div>
  <span class="slide-arrow prev"><svg width="27" height="26"><path d="M17 6l-7 7 7 7" stroke="#111" stroke-width="4" fill="none"/></svg></span>
  <span class="slide-arrow next"><svg width="27" height="26"><path d="M10 6l7 7-7 7" stroke="#111" stroke-width="4" fill="none"/></svg></span>
</section>

<section class="abs service" style="left:108px">
  <div class="service-head">
    <div class="service-icon" role="img" aria-label="Orange-roofed house icon" style="background:linear-gradient(160deg,#f08a3c,#c9c3bb)"></div>
    <h2 class="service-title">Residential</h2>
  </div>
  <ul>
    <li><svg width="8" height="7"><path d="M1 3.5l2 2 4-4.5" stroke="#222" stroke-width="1.6" fill="none"/></svg>Lorem ipsum dolor sit amet, consectetur.</li>
    <li><svg width="8" height="7"><path d="M1 3.5l2 2 4-4.5" stroke="#222" stroke-width="1.6" fill="none"/></svg>Nam venenatis nibh commodo neque.</li>
    <li><svg width="8" height="7"><path d="M1 3.5l2 2 4-4.5" stroke="#222" stroke-width="1.6" fill="none"/></svg>Curabitur vestibulum odio eu risus.</li>
  </ul>
  <div class="service-rule"><span class="read-more">Read More →</span></div>
</section>

<section class="abs service" style="left:354px">
  <div class="service-head">
    <div class="service-icon" role="img" aria-label="Blue glass office tower icon" style="background:linear-gradient(160deg,#6f8fae,#c3ccd4)"></div>
    <h2 class="service-title">Commercial</h2>
  </div>
  <ul>
    <li><svg width="8" height="7"><path d="M1 3.5l2 2 4-4.5" stroke="#222" stroke-width="1.6" fill="none"/></svg>Lorem ipsum dolor sit amet, consectetur.</li>
    <li><svg width="8" height="7"><path d="M1 3.5l2 2 4-4.5" stroke="#222" stroke-width="1.6" fill="none"/></svg>Nam venenatis nibh commodo neque.</li>
    <li><svg width="8" height="7"><path d="M1 3.5l2 2 4-4.5" stroke="#222" stroke-width="1.6" fill="none"/></svg>Curabitur vestibulum odio eu risus.</li>
  </ul>
  <div class="service-rule"><span class="read-more">Read More →</span></div>
</section>

<section class="abs service" style="left:600px">
  <div class="service-head">
    <div class="service-icon" role="img" aria-label="Grey building tower icon" style="background:linear-gradient(160deg,#b9bcbf,#e2e3e4)"></div>
    <h2 class="service-title">Insurance</h2>
  </div>
  <ul>
    <li><svg width="8" height="7"><path d="M1 3.5l2 2 4-4.5" stroke="#222" stroke-width="1.6" fill="none"/></svg>Lorem ipsum dolor sit amet, consectetur.</li>
    <li><svg width="8" height="7"><path d="M1 3.5l2 2 4-4.5" stroke="#222" stroke-width="1.6" fill="none"/></svg>Nam venenatis nibh commodo neque.</li>
    <li><svg width="8" height="7"><path d="M1 3.5l2 2 4-4.5" stroke="#222" stroke-width="1.6" fill="none"/></svg>Curabitur vestibulum odio eu risus.</li>
  </ul>
  <div class="service-rule"><span class="read-more">Read More →</span></div>
</section>

<section class="abs welcome">
  <h1>Welcome to<span>Felix Morrow &amp; Co.</span></h1>
  <p>Lorem Ipsum is simply dummy text of the printing and typesetting industry. Lorem Ipsum has been the industry's standard dummy text ever since the 1500s, when an unknown printer took a galley of type and scrambled it to make a type specimen book. It has survived not only five centuries, but also the leap into electronic typesetting, remaining essentially unchanged.</p>
</section>

<h3 class="abs reasons-title">Three Reasons to Choose Us</h3>

<div class="abs reason" style="left:100px">
  <svg width="150" height="56" viewBox="0 0 150 56" aria-hidden="true">
    <path d="M33 20l6 6-6 6M124 20l6 6-6 6M130 20l6 6-6 6" stroke="#ccc" stroke-width="1.3" fill="none"/>
    <circle cx="75" cy="25" r="24" fill="var(--beige)" stroke="#d8cfb6"/>
    <path d="M64 25l8 8 14-16" stroke="#4a9a2e" stroke-width="5" fill="none"/>
    <circle cx="101" cy="40" r="12" fill="#fff"/><circle cx="101" cy="40" r="10" fill="#4a9a2e"/>
    <text x="101" y="44" font-size="11" font-family="Arimo,sans-serif" fill="#fff" text-anchor="middle">1</text>
  </svg>
  <div class="reason-text">Our work is<strong>Guaranteed</strong></div>
</div>

<div class="abs reason" style="left:258px">
  <svg width="150" height="56" viewBox="0 0 150 56" aria-hidden="true">
    <path d="M33 20l6 6-6 6M124 20l6 6-6 6M130 20l6 6-6 6" stroke="#ccc" stroke-width="1.3" fill="none"/>
    <circle cx="75" cy="25" r="24" fill="var(--beige)" stroke="#d8cfb6"/>
    <rect x="62" y="18" width="16" height="12" fill="#4a9a2e"/><path d="M78 21h6l4 5v4H78z" fill="#4a9a2e"/>
    <circle cx="67" cy="32" r="2.5" fill="#4a9a2e"/><circle cx="83" cy="32" r="2.5" fill="#4a9a2e"/>
    <circle cx="101" cy="40" r="12" fill="#fff"/><circle cx="101" cy="40" r="10" fill="#4a9a2e"/>
    <text x="101" y="44" font-size="11" font-family="Arimo,sans-serif" fill="#fff" text-anchor="middle">2</text>
  </svg>
  <div class="reason-text">Always arrive<strong>On Time</strong></div>
</div>

<div class="abs reason" style="left:415px">
  <svg width="150" height="56" viewBox="0 0 150 56" aria-hidden="true">
    <path d="M124 20l6 6-6 6M130 20l6 6-6 6" stroke="#ccc" stroke-width="1.3" fill="none"/>
    <circle cx="75" cy="25" r="24" fill="var(--beige)" stroke="#d8cfb6"/>
    <rect x="64" y="22" width="5" height="12" fill="#4a9a2e"/>
    <path d="M70 22l5-9c2 0 3 2 2 5h7c2 0 2 3 1 4l-2 11H70z" fill="#4a9a2e"/>
    <circle cx="101" cy="40" r="12" fill="#fff"/><circle cx="101" cy="40" r="10" fill="#4a9a2e"/>
    <text x="101" y="44" font-size="11" font-family="Arimo,sans-serif" fill="#fff" text-anchor="middle">2</text>
  </svg>
  <div class="reason-text">100%<strong>Satisfaction</strong></div>
</div>

<aside class="abs quote">
  <div class="quote-art" role="img" aria-label="Red paint splash with a paintbrush illustration"></div>
  <div class="quote-bar">CLICK FOR A QUOTE
    <svg width="15" height="15"><circle cx="7.5" cy="7.5" r="7" fill="#ddd"/><path d="M4 7.5h6M8 5l2.5 2.5L8 10" stroke="#444" stroke-width="1.4" fill="none"/></svg>
  </div>
</aside>

<aside class="abs badge">
  <div class="badge-shape" role="img" aria-label="Trade association membership badge"></div>
</aside>

<footer class="abs footer">
  <div class="abs footer-links">
    <h4>QUICK LINKS</h4>
    <ul>
      <li>Home</li><li>Residential</li><li>Commercial</li><li>Insurance</li><li>Contact Us</li>
    </ul>
  </div>
  <div class="abs footer-contact">
    Address: PO Box 418 Kelvin Grove, 4059<br>
    Email: hello@felixmorrow.com.au
    <div class="footer-call">Call NOW!<b>(07) 3190 4826</b></div>
  </div>
  <div class="abs footer-copy">Copyright © 2012 Felix Morrow &amp; Co. All Rights Reserved.</div>
  <div class="abs footer-follow">Follow us:&nbsp;
    <span class="social"></span><span class="social"></span><span class="social"></span><span class="social"></span>
  </div>
</footer>

</body>
</html>
```